Stylish Design With Simple UI For Appointment Site

Note: Logo file now attached. Extra credit to anyone who offers basic HTML templates in the final deliverable, incorporating the individual components of the design (using DIVs and CSS).

There are two key requirements for this site:

1. It makes our site look like one of the most professional of its kind. We want to look the part;
2. It has a very simple, straight-forward user interface. We're nothing without being intuitive.

Our site will be used by other businesses to set up their own online booking systems.

Logo samples attached. The colour scheme is not yet set but two possible options are:

1. Dark (#323B3A) & Blue (#12B5D4) on White background
2. White & Yellow (#FEF102) on Grey (#3A3A3C) background

For inspiration, and an idea of what we like, take a look at quillbarn.com - it's very clear and eye-catching, although its pages are longer than we would like ours to be. Oh but we don't need a chimp! Instead of the section with the chimp in, we would like a changing image headline section on the home page, in the style of fellgarde.co.uk (with a less high image; we have attached one image which you may want to try out with this, but happy to see other ideas).

Any graphics included must be royalty free and free for commercial use. Fonts should be readily available and specified.

We would like to see the design applied to the following pages:

1. The main public home page (features header, login prompt, menu, changing image banner with headlines, main body, footer menu).
2. A secondary public page (features a similar layout to home page but without image headline banner, includes extra panels/body detail).
3. The Control Panel page (features several list panels and an add appointment button).
4. A list-style administration page (with popup item editor window).
5. A settings administration page (with form).

In that order, a sample walk-through design spec will be attached.

To summarise, we are looking for someone to put forward not only a design but something which also focuses on the user interface. The designer should consider all of the examples and guidance given, but shouldn't let that limit any innovation.

Happy to respond to any questions and give constant feedback.

Thank you.

-*-*-*-*-*-*-*-*-*-*-*-*-*-*-*-*-

Update, 18th Nov 2011:

1. I'm about the upload the logos so you can incorporate these into your designs.

2. A UI question of mine is how to move from a list view (e.g. Resources) to editing one of those items in the list. In the spec document I showed a popup editor for these items but I don't know if that's the best thing to do. Happy to see other ideas on this - whatever the best user experience would be.

3. On the designs in the spec document I've not included any help functionality. It would be good to include pieces of guidance on each page of the administration area to help the user - guess these could either be info panels on the pages themselves or info popups. Again, would be good to see some ideas in the designs.

Also, just to be clear, I am really looking for something that looks like a modern innovative "web app" rather than it looking like a promotional corporate web site.

Target Market(s)

Owners of businesses of all types (e.g. salons, small hotels, surgeries, etc).

Industry/Entity Type

Commercial

Requirements
Must have
• Headline image transition panel on home page.

Layout, graphic and font styles along similar lines to quillbarn.com, fellgarde.co.uk, etc.
Nice to have
• Blog feed panel on the home page.

Innovative ideas for improvements to the spec.
Should not have
• Anything which can't be practically rendered when the design is converted to HTML.

Should not be overly influenced by the layout and style in the attached spec - that should just be a guide to the content and layout of the site.

```html
<!DOCTYPE html>
<html lang="en">
<head>
<meta charset="utf-8">
<title>Slotwise – Home</title>
<link href="https://fonts.googleapis.com/css2?family=Arimo:wght@400;700&display=swap" rel="stylesheet">
<style>
  :root {
    --page-bg: #3b3b3d;
    --page-bg-top: #2e2e30;
    --panel: #4b4b4d;
    --panel-edge: #555557;
    --field: #1b1b1c;
    --text: #ffffff;
    --text-soft: #d6d6d6;
    --text-muted: #a9a9ab;
    --accent: #f0b92a;
    --accent-deep: #e2a514;
    --nav-tab: #4a4a4c;
    --footer: #1d1d1f;
    --slide-dark: #000000;
  }
  * { box-sizing: border-box; margin: 0; padding: 0; }
  html, body { width: 1200px; height: 1127px; overflow: hidden; }
  body {
    font-family: "Arimo", Arial, sans-serif;
    background: linear-gradient(180deg, var(--page-bg-top) 0, var(--page-bg) 300px, var(--page-bg) 100%);
    color: var(--text);
    position: relative;
  }
  .abs { position: absolute; }

  /* Header */
  .brand { left: 70px; top: 50px; display: flex; align-items: center; gap: 16px; }
  .brand-mark { width: 30px; height: 30px; background: var(--accent); }
  .brand-name { font-size: 42px; letter-spacing: 6px; color: var(--text); font-weight: 400; }

  .login-label { font-size: 16px; color: var(--text-soft); right: 250px; text-align: right; }
  .login-field {
    left: 954px; width: 218px; height: 43px; background: var(--field);
    border: 1px solid #111; box-shadow: inset 0 2px 4px rgba(0,0,0,.7), 0 1px 0 rgba(255,255,255,.08);
  }
  .forgot { left: 971px; top: 188px; font-size: 14px; color: var(--text-soft); text-decoration: underline; }
  .login-btn {
    left: 1099px; top: 179px; width: 73px; height: 35px; font-size: 16px; color: var(--text);
    background: linear-gradient(#5d6373, #454a58); border: 1px solid #6b7080;
    display: flex; align-items: center; justify-content: center;
  }

  /* Navigation */
  .main-nav { left: 62px; top: 220px; height: 64px; display: flex; }
  .main-nav a {
    display: flex; align-items: center; justify-content: center; height: 64px;
    font-size: 19px; color: var(--text-soft); text-decoration: none;
    background: linear-gradient(#545456, #434345); border-right: 1px solid #333;
  }
  .main-nav a.is-current { background: linear-gradient(#f3c230, var(--accent-deep)); color: #1a1a1a; }
  .lang { left: 956px; top: 247px; font-size: 15px; color: var(--text); display: flex; align-items: center; gap: 8px; }
  .lang-flag { width: 17px; height: 11px; background: #8a3a4a; }

  /* Slider */
  .hero { left: 29px; top: 284px; width: 1147px; height: 377px; background: var(--panel); border-radius: 0 0 8px 8px; }
  .hero-slide { left: 72px; top: 293px; width: 1063px; height: 360px; background: var(--slide-dark); border-radius: 0 0 10px 10px; overflow: hidden; }
  .hero-photo {
    position: absolute; left: 0; top: 0; width: 430px; height: 360px;
    background: radial-gradient(ellipse at 25% 60%, #e6e8ea 0, #b8bcc0 35%, #6d6f72 60%, #1a1a1a 80%, #000 100%);
  }
  .hero-copy { left: 517px; top: 410px; width: 560px; font-size: 16px; line-height: 33px; color: var(--text-soft); }
  .signup { left: 876px; top: 488px; display: flex; align-items: center; }
  .signup-btn {
    margin-left: -8px; padding: 8px 22px 8px 20px; border-radius: 0 18px 18px 0;
    background: linear-gradient(#ffffff, #c9c9c9); color: #111; font-size: 19px; font-weight: 700; font-style: italic;
  }
  .arrow { top: 456px; }
  .dots { left: 992px; top: 621px; display: flex; gap: 12px; }
  .dots span { width: 13px; height: 13px; border-radius: 50%; background: #8e8e90; }
  .dots span.is-active { background: #ececec; }

  /* Content panels */
  .content { left: 29px; top: 690px; width: 1147px; height: 294px; background: var(--panel); border-radius: 10px; }
  .content-divider { left: 597px; top: 690px; width: 3px; height: 294px; background: linear-gradient(90deg, #3a3a3c, #555557); }
  .info h2 { font-size: 29px; font-weight: 400; color: var(--accent); margin-bottom: 18px; }
  .info p { font-size: 13.4px; line-height: 24px; color: var(--text); width: 510px; }
  .view-more { font-size: 14px; color: var(--accent); text-decoration: underline; top: 929px; }

  /* Footer */
  .footer { left: 0; top: 1004px; width: 1200px; height: 123px; background: var(--footer); border-top: 3px solid #2c2c2e; }
  .footer-nav { left: 32px; top: 1032px; font-size: 13px; color: var(--text-muted); display: flex; gap: 12px; }
  .footer-nav span.sep { color: #777; }
  .copyright { left: 32px; top: 1064px; font-size: 13px; color: var(--text-muted); }
  .connect { left: 954px; top: 1034px; font-size: 13px; color: var(--text-muted); }
  .social { left: 954px; top: 1063px; display: flex; gap: 22px; }
  .social span { width: 26px; height: 26px; background: #6c6c70; border-radius: 2px; }
</style>
</head>
<body>

<header>
  <div class="abs brand"><span class="brand-mark"></span><span class="brand-name">SLOTWISE</span></div>

  <label class="abs login-label" style="top:70px">user name :</label>
  <div class="abs login-field" style="top:60px"></div>
  <label class="abs login-label" style="top:132px">Pass word :</label>
  <div class="abs login-field" style="top:121px"></div>
  <a class="abs forgot">forgot password?</a>
  <div class="abs login-btn">Log In</div>

  <nav class="abs main-nav">
    <a class="is-current" style="width:123px">HOME</a>
    <a style="width:163px">FEATURES</a>
    <a style="width:135px">PRICING</a>
    <a style="width:190px">CONTACT US</a>
  </nav>
  <div class="abs lang"><span class="lang-flag"></span>United States - English
    <svg width="12" height="8" viewBox="0 0 12 8"><path d="M0 0h12L6 7z" fill="#fff"/></svg>
  </div>
</header>

<section>
  <div class="abs hero"></div>
  <div class="abs hero-slide">
    <div class="hero-photo" role="img" aria-label="Close-up photo of a clock face"></div>
  </div>
  <svg class="abs arrow" style="left:36px" width="18" height="34" viewBox="0 0 18 34"><path d="M15 2L3 17l12 15" stroke="#1a1a1a" stroke-width="3" fill="none"/></svg>
  <svg class="abs arrow" style="left:1150px" width="18" height="34" viewBox="0 0 18 34"><path d="M3 2l12 15L3 32" stroke="#1a1a1a" stroke-width="3" fill="none"/></svg>
  <p class="abs hero-copy">Corvinus Tell are also reproduced in their exact original form, accompanied by English versions from the 1914 translation by H. Dunmore.</p>
  <div class="abs signup">
    <svg width="44" height="64" viewBox="0 0 44 64"><path d="M10 28V16a12 12 0 0 1 24 0v12" stroke="#bbb" stroke-width="6" fill="none"/><rect x="2" y="28" width="40" height="34" rx="3" fill="#9a9a9a"/></svg>
    <span class="signup-btn">Sign Up</span>
  </div>
  <div class="abs dots"><span class="is-active"></span><span></span><span></span><span></span><span></span></div>
</section>

<main>
  <div class="abs content"></div>
  <div class="abs content-divider"></div>
  <article class="abs info" style="left:66px;top:710px">
    <h2>Make Your Self Available</h2>
    <p>The standard chunk of Lorem Ipsum used since the 1500s is reproduced below for those interested. Sections 1.10.32 and 1.10.33 from "de Finibus Bonorum et Malorum" by Corvinus Tell are also reproduced in their exact original form, accompa-nied by English versions from the 1914 translation combined with a handful of model sentence structures, to generate Lorem Ipsum which looks reasonable. humour, or non-characteristic words etc.</p>
  </article>
  <a class="abs view-more" style="left:497px">View more</a>
  <article class="abs info" style="left:630px;top:710px">
    <h2>What’s Happening?</h2>
    <p>The standard chunk of Lorem Ipsum used since the 1500s is reproduced below for those interested. Sections 1.10.32 and 1.10.33 from "de Finibus Bonorum et Malorum" by Corvinus Tell are also reproduced in their exact original form, accompa-nied by English versions from the 1914 translation combined with a handful of model sentence structures, to generate Lorem Ipsum which looks reasonable. humour, or non-characteristic words etc.</p>
  </article>
  <a class="abs view-more" style="left:1062px">View more</a>
</main>

<footer>
  <div class="abs footer"></div>
  <nav class="abs footer-nav">
    <span>Home</span><span class="sep">|</span><span>Features</span><span class="sep">|</span><span>Pricing</span><span class="sep">|</span><span>Contact US</span><span class="sep">|</span><span>Sitemap</span>
  </nav>
  <p class="abs copyright">Copyright © 2011 www.slotwise.com &nbsp;All rights reserved</p>
  <p class="abs connect">Connect with us :</p>
  <div class="abs social"><span></span><span></span><span></span><span></span><span></span></div>
</footer>

</body>
</html>
```